Promotion Layer (UI Design)

What we need is not a classical App Design.
We need a UI Design for a SDK, which appears as Layer in different apps.
The layer will contain a list/library which will show cool goodies for the app user.

The attached file will give you all the details you need to start.

Note: The Screenshots do show app content. But these are just place holders.
The content is NOT part of the design task. Because we just provide the layer...

The crucial part of this task is, to create a UI design, that is stylish, simple and does not harm the 3rd party app, where it will be showed. While you design it, allways try to think "do I like this, when it appears in my own app"

Your files should be made in the right size/dimensions of ios.

Industry/Entity Type

Library

Font styles to use
Sans Serif

Requirements
Must have
• Must fit the iOS 7 Style

```html
<!DOCTYPE html>
<html lang="en">
<head>
<meta charset="utf-8">
<title>Promotion Layer – Offer Detail</title>
<link rel="stylesheet" href="https://fonts.googleapis.com/css2?family=Arimo:wght@400;700&display=swap">
<style>
  :root {
    --bar-black: #121212;
    --nav-black: #161617;
    --ios-blue: #1a8cff;
    --content-bg: #efeff4;
    --toolbar-bg: #f8f8f8;
    --hairline: #c8c7cc;
    --text-dark: #111111;
    --white: #ffffff;
    --offer-orange: #ff9500;
    --photo-skin: #e9b89c;
    --photo-warm: #c98866;
    --photo-pink: #d9b3c2;
  }
  * { box-sizing: border-box; margin: 0; padding: 0; }
  html, body {
    width: 713px;
    height: 1200px;
    overflow: hidden;
    background: var(--content-bg);
    font-family: "Arimo", Helvetica, Arial, sans-serif;
    color: var(--text-dark);
  }
  .screen {
    position: relative;
    width: 713px;
    height: 1200px;
    overflow: hidden;
    background: var(--content-bg);
  }
  .status-bar {
    position: absolute; left: 0; top: 0;
    width: 100%; height: 52px;
    background: var(--bar-black);
    color: var(--white);
    font-size: 25px;
    display: flex; align-items: center;
    padding: 0 18px;
  }
  .status-left { display: flex; align-items: center; gap: 8px; flex: 1; }
  .status-time { position: absolute; left: 0; right: 0; text-align: center; font-weight: 700; pointer-events: none; }
  .status-right { display: flex; align-items: center; gap: 10px; }
  .nav-bar {
    position: absolute; left: 0; top: 52px;
    width: 100%; height: 88px;
    background: var(--nav-black);
    display: flex; align-items: center; justify-content: space-between;
    padding: 0 18px;
    font-size: 36px;
    color: var(--ios-blue);
  }
  .nav-back { display: flex; align-items: center; gap: 10px; }
  .offer-header {
    position: absolute; left: 38px; top: 158px;
    display: flex; align-items: center; gap: 30px;
    font-size: 34px;
  }
  .offer-icon {
    width: 64px; height: 64px;
    border-radius: 8px;
    background: var(--offer-orange);
    display: flex; align-items: center; justify-content: center;
  }
  .offer-photo {
    position: absolute; left: 38px; top: 243px;
    width: 638px; height: 364px;
    background: linear-gradient(120deg, var(--photo-skin) 0%, var(--photo-warm) 40%, var(--photo-pink) 55%, var(--photo-skin) 80%, #f1d6c4 100%);
  }
  .offer-title {
    position: absolute; left: 38px; top: 624px;
    width: 640px;
    font-size: 34px; font-weight: 700; line-height: 45px;
  }
  .offer-body {
    position: absolute; left: 38px; top: 730px;
    width: 630px;
    font-size: 33px; line-height: 44.5px;
  }
  .action-toolbar {
    position: absolute; left: 0; top: 1108px;
    width: 100%; height: 92px;
    background: var(--toolbar-bg);
    border-top: 1px solid var(--hairline);
    display: flex; align-items: center; justify-content: space-between;
    padding: 0 34px 0 34px;
    font-size: 34px;
    color: var(--ios-blue);
  }
</style>
</head>
<body>
<div class="screen">
  <header class="status-bar">
    <div class="status-left">
      <svg width="84" height="16" viewBox="0 0 84 16" aria-hidden="true">
        <circle cx="8" cy="8" r="6.5" fill="#fff"/>
        <circle cx="24" cy="8" r="6.5" fill="#fff"/>
        <circle cx="40" cy="8" r="6.5" fill="#fff"/>
        <circle cx="56" cy="8" r="5.8" fill="none" stroke="#fff" stroke-width="1.4"/>
        <circle cx="72" cy="8" r="5.8" fill="none" stroke="#fff" stroke-width="1.4"/>
      </svg>
      <span class="carrier">NOVA</span>
      <svg width="28" height="22" viewBox="0 0 28 22" aria-hidden="true">
        <path d="M2 8 A17 17 0 0 1 26 8" fill="none" stroke="#fff" stroke-width="3"/>
        <path d="M7 13 A10 10 0 0 1 21 13" fill="none" stroke="#fff" stroke-width="3"/>
        <circle cx="14" cy="18" r="3" fill="#fff"/>
      </svg>
    </div>
    <div class="status-time">4:21 PM</div>
    <div class="status-right">
      <svg width="14" height="26" viewBox="0 0 14 26" aria-hidden="true">
        <path d="M2 7 L12 18 L7 23 L7 3 L12 8 L2 19" fill="none" stroke="#fff" stroke-width="2"/>
      </svg>
      <span>22%</span>
      <svg width="52" height="24" viewBox="0 0 52 24" aria-hidden="true">
        <rect x="1" y="2" width="44" height="20" rx="3" fill="none" stroke="#fff" stroke-width="2"/>
        <rect x="4" y="5" width="9" height="14" fill="#fff"/>
        <rect x="47" y="8" width="3" height="8" fill="#fff"/>
      </svg>
    </div>
  </header>

  <nav class="nav-bar">
    <div class="nav-back">
      <svg width="22" height="38" viewBox="0 0 22 38" aria-hidden="true">
        <path d="M19 3 L4 19 L19 35" fill="none" stroke="#1a8cff" stroke-width="4" stroke-linecap="round" stroke-linejoin="round"/>
      </svg>
      <span>Back</span>
    </div>
    <span class="nav-done">Finished</span>
  </nav>

  <div class="offer-header">
    <div class="offer-icon">
      <svg width="40" height="36" viewBox="0 0 40 36" aria-hidden="true">
        <path d="M10 3 H30 L37 12 L20 33 L3 12 Z M3 12 H37 M14 3 L12 12 L20 33 L28 12 L26 3" fill="none" stroke="#fff" stroke-width="2.2" stroke-linejoin="round"/>
      </svg>
    </div>
    <span class="offer-name">Diamond 40% Discount</span>
  </div>

  <div class="offer-photo" role="img" aria-label="Photo of a hand holding up a large pink diamond ring"></div>

  <h1 class="offer-title">Sed sit amet facilisis ipsum sed tempor justo</h1>

  <p class="offer-body">Nunc volutpat odio sit amet lectus gravida faucibus. Morbi vitae justo dictum, placerat mauris sed, suscipit mauris. In at dui ullamcorper, pretium dolor at, lacinia nisi. Morbi aliquet sapien elit, id accumsan nunc facilisis eu. Aliquam vitae porttitor felis. Fusce mattis augue in orci tincidunt hendrerit in non enim. Praesent eget sapien ut mollis.</p>

  <footer class="action-toolbar">
    <span>Redeem</span>
    <span>Add to PassKeep</span>
    <span>Share</span>
  </footer>
</div>
</body>
</html>
```